Financial firm simple design

Classic business card design for a financial fund. 2 sided card- white on both sides.. One with just the company name centered and the other w the info. info included on that is :

Name
Company position
phone number
fax
email
website

Financial

```html
<!DOCTYPE html>
<html lang="en">
<head>
<meta charset="utf-8">
<title>Norvale Investments – Business Card</title>
<link href="https://fonts.googleapis.com/css2?family=Cinzel:wght@400;500&family=Lato:wght@400;700&display=swap" rel="stylesheet">
<style>
  :root {
    --navy: #12407c;
    --navy-deep: #0d3566;
    --ink: #1b1b1b;
    --paper: #ffffff;
    --backdrop: #e9e9ec;
    --line: #2b5592;
  }
  * { box-sizing: border-box; margin: 0; padding: 0; }
  html, body {
    width: 1200px; height: 579px; overflow: hidden;
    background: var(--backdrop);
  }
  .stage {
    position: relative; width: 1200px; height: 579px;
    display: flex; align-items: center; justify-content: center; gap: 60px;
  }
  .card {
    position: relative; width: 520px; height: 300px;
    background: var(--paper); border-radius: 16px; overflow: hidden;
    box-shadow: 0 6px 18px rgba(0,0,0,.18);
  }

  /* Info side */
  .brand-row {
    position: absolute; top: 34px; left: 0; right: 0;
    display: flex; align-items: center; gap: 14px;
  }
  .brand-row .bar { height: 14px; background: var(--navy); flex: 1; }
  .brand-row .bar.left { flex: 0 0 110px; }
  .brand-name {
    font-family: "Cinzel", serif; font-weight: 500; font-size: 20px;
    color: var(--navy); letter-spacing: .5px; white-space: nowrap;
  }
  .person {
    position: absolute; top: 66px; right: 22px; text-align: right;
    font-family: "Cinzel", serif; color: var(--navy);
  }
  .person .name { font-size: 19px; font-weight: 500; letter-spacing: .5px; }
  .person .role { font-size: 12px; font-variant: small-caps; letter-spacing: .8px; margin-top: 1px; }
  .rule {
    position: absolute; top: 118px; left: 0; right: 0;
    height: 1.5px; background: var(--line);
  }
  .contacts {
    position: absolute; left: 26px; top: 182px; list-style: none;
    font-family: "Lato", sans-serif; font-weight: 700; font-size: 12.5px;
    color: var(--navy-deep);
  }
  .contacts li { display: flex; align-items: center; gap: 12px; height: 19px; }
  .contacts svg { width: 14px; height: 12px; fill: var(--navy-deep); }
  .web-band {
    position: absolute; left: 0; right: 0; bottom: 0; height: 42px;
    background: var(--navy); display: flex; align-items: center; justify-content: center;
    font-family: "Lato", sans-serif; font-weight: 700; font-size: 15px;
    letter-spacing: 1.5px; color: var(--paper);
  }

  /* Name side */
  .frame {
    position: absolute; inset: 10px;
    border: 3px solid var(--navy); border-radius: 12px;
  }
  .front-name {
    position: absolute; inset: 0; display: flex; align-items: center; justify-content: center;
    font-family: "Cinzel", serif; font-weight: 500; font-size: 30px;
    color: var(--navy); letter-spacing: 1px;
  }
</style>
</head>
<body>
<main class="stage">
  <section class="card card-info" aria-label="Card back with contact details">
    <div class="brand-row">
      <span class="bar left"></span>
      <span class="brand-name">Norvale Investments</span>
      <span class="bar"></span>
    </div>
    <div class="person">
      <div class="name">YOUR NAME</div>
      <div class="role">Designation</div>
    </div>
    <div class="rule"></div>
    <ul class="contacts">
      <li>
        <svg viewBox="0 0 14 12" aria-hidden="true"><path d="M1 3 Q7 -1 13 3 L12 5 L9.5 4 L9.5 3 Q7 2 4.5 3 L4.5 4 L2 5 Z"/><rect x="3" y="6" width="8" height="5" rx="1"/></svg>
        <span>+1 800-555-0147</span>
      </li>
      <li>
        <svg viewBox="0 0 14 12" aria-hidden="true"><rect x="3.5" y="0" width="7" height="3.5"/><rect x="0.5" y="4" width="13" height="5" rx="1"/><rect x="3.5" y="8" width="7" height="4"/></svg>
        <span>+33 (0)1 55 20 31 68</span>
      </li>
      <li>
        <svg viewBox="0 0 14 12" aria-hidden="true"><path d="M0.5 1.5 H13.5 V10.5 H0.5 Z M1.5 2.5 L7 7 L12.5 2.5 Z" fill-rule="evenodd"/></svg>
        <span>info@norvaleinvest.com</span>
      </li>
    </ul>
    <div class="web-band">www.norvaleinvest.com</div>
  </section>

  <section class="card card-front" aria-label="Card front with company name">
    <div class="frame"></div>
    <div class="front-name">Norvale Investments</div>
  </section>
</main>
</body>
</html>
```